We Need a GREAT Looking Sales Flyer!

Our small, boutique fitness facility needs a new flyer which highlights a new entry level fitness program that we are launching.

The flyer should be visually appealing as we will be handing a full color version to the potential member during our sales process.

I have attached:
- a word document which includes text
-Photos that can be used. Not all need to be used. These are to be used as you feel appropriate
- Our Logo

```html
<!DOCTYPE html>
<html lang="en">
<head>
<meta charset="utf-8">
<title>The Ultimate Kickstart – PulseForge</title>
<link rel="stylesheet" href="https://fonts.googleapis.com/css2?family=Oswald:wght@500;700&family=Lexend:wght@400;600;700&display=swap">
<style>
  :root {
    --ink: #0a0a0c;
    --ink-soft: #1b1c20;
    --blue: #0a9bf2;
    --blue-glow: #17a7ff;
    --yellow: #f7ee10;
    --yellow-deep: #fff200;
    --white: #ffffff;
    --muted: #e9e9ee;
    --photo-top: #d9cfd3;
    --photo-bottom: #8d9290;
  }
  * { box-sizing: border-box; margin: 0; padding: 0; }
  html, body { width: 1009px; height: 1200px; overflow: hidden; background: var(--ink); }
  .flyer {
    position: relative; width: 1009px; height: 1200px; overflow: hidden;
    background: var(--ink);
    font-family: "Lexend", sans-serif; color: var(--white);
  }
  .backdrop { position: absolute; inset: 0; }
  .abs { position: absolute; }

  .kicker {
    left: 0; width: 1009px; top: 44px; text-align: center;
    font-family: "Oswald", sans-serif; font-weight: 700; font-size: 54px; line-height: 1;
    color: var(--yellow-deep); transform: skewX(-10deg); letter-spacing: -1px;
  }
  .headline {
    left: 0; width: 1009px; top: 88px; text-align: center;
    font-family: "Oswald", sans-serif; font-weight: 700; font-size: 102px; line-height: 1;
    color: var(--blue-glow); transform: skewX(-10deg) scaleY(1.08); letter-spacing: -2px;
    text-shadow: 0 0 14px rgba(23,167,255,.75), 0 0 30px rgba(23,167,255,.45);
  }
  .proof-band {
    left: 71px; top: 197px; width: 866px; height: 38px;
    background: var(--blue); clip-path: polygon(1% 0, 100% 0, 99% 100%, 0 100%);
    display: flex; align-items: center; justify-content: center;
    font-size: 19px; font-weight: 600; font-style: italic; letter-spacing: -.2px;
  }
  .meal-line { left: 80px; top: 248px; font-size: 21px; }
  .meal-line strong { font-weight: 700; }

  .section-title {
    left: 52px; top: 310px;
    font-family: "Oswald", sans-serif; font-weight: 700; font-size: 56px; line-height: 1;
    transform: scaleX(.82); transform-origin: left;
  }
  .section-rule { left: 52px; top: 372px; width: 330px; height: 3px;
    background: linear-gradient(90deg, var(--blue), rgba(10,155,242,0)); }
  .offer-lead { left: 52px; top: 382px; font-size: 25px; line-height: 32px; }

  .yellow-panel { left: 0; top: 0; }
  .photo {
    left: 560px; top: 320px; width: 400px; height: 760px;
    background: linear-gradient(180deg, var(--photo-top), var(--photo-bottom));
    border-radius: 180px 180px 24px 24px; opacity: .92;
  }

  .promise-band {
    left: 47px; top: 455px; width: 962px; height: 51px;
    background: var(--blue); clip-path: polygon(1.2% 0, 100% 0, 100% 100%, 0 100%);
    display: flex; align-items: center; padding-left: 18px; font-size: 25px;
  }
  .promise-band strong { font-weight: 700; margin-left: 7px; }

  .benefits { left: 52px; top: 528px; width: 380px; list-style: none; }
  .benefits li {
    position: relative; padding-left: 31px; font-size: 19.5px; line-height: 22.5px; margin-bottom: 23px;
  }
  .benefits li svg { position: absolute; left: 0; top: 6px; }

  .price-old {
    left: 188px; top: 858px; font-size: 46px; font-weight: 400; color: var(--muted);
    transform: rotate(-12deg); letter-spacing: 1px;
  }
  .price-old::after {
    content: ""; position: absolute; left: -30px; right: -30px; top: 50%; height: 6px;
    background: var(--blue); transform: rotate(-4deg);
  }
  .limited-tag {
    left: 196px; top: 1090px; width: 222px; height: 86px; background: var(--yellow);
    transform: rotate(-14deg); display: flex; align-items: center; justify-content: center;
    text-align: center; color: var(--blue); font-weight: 700; font-size: 30px; line-height: 26px;
  }
  .price-card {
    left: 152px; top: 918px; width: 257px; height: 162px; background: var(--blue);
    transform: rotate(-14deg); display: flex; align-items: center; justify-content: center; gap: 10px;
  }
  .price-card .cta {
    font-family: "Oswald", sans-serif; font-weight: 500; font-size: 19px; line-height: 17px;
    text-align: center; transform: scaleX(.75);
  }
  .price-card .amount {
    font-family: "Oswald", sans-serif; font-weight: 700; font-size: 122px; line-height: 1;
    letter-spacing: -4px; transform: scaleX(.82);
  }

  .brand { left: 640px; top: 1080px; width: 340px; text-align: center; }
  .brand-name { font-size: 58px; font-weight: 700; letter-spacing: -1px; line-height: 1; }
  .brand-tagline { font-size: 13px; letter-spacing: 4px; margin-top: 6px; }
</style>
</head>
<body>
<main class="flyer">
  <svg class="backdrop" width="1009" height="1200" aria-hidden="true">
    <polygon points="420,380 1009,130 1009,520 600,640" fill="#16171b"/>
    <polygon points="0,700 480,520 480,1200 0,1200" fill="#111216"/>
    <polygon points="500,506 1009,482 1009,972 500,1055" fill="#f7ee10"/>
  </svg>

  <div class="abs photo" role="img" aria-label="Photo of a woman in a tank top and patterned leggings doing a dumbbell lunge"></div>

  <p class="abs kicker">CHANGE BEGINS NOW!</p>
  <h1 class="abs headline">THE ULTIMATE KICKSTART</h1>
  <p class="abs proof-band">The Fitness Program that is responsible for transforming over 924+ lives!</p>
  <p class="abs meal-line"><strong>CUSTOM</strong> Meal Plan designed specifically for Your &amp; Your Body Type</p>

  <h2 class="abs section-title">WHAT YOU GET</h2>
  <div class="abs section-rule"></div>
  <p class="abs offer-lead">Unlimited Group Training Designed<br>Specifically to Sculpt &amp; Tone the body.</p>

  <p class="abs promise-band">The Life That You Envision Is <strong>POSSIBLE!</strong></p>

  <ul class="abs benefits">
    <li><svg width="8" height="12" viewBox="0 0 8 12"><path d="M1 1l5 5-5 5" stroke="#0a9bf2" stroke-width="2" fill="none"/></svg>Two Detailed Body Scans to<br>track results</li>
    <li><svg width="8" height="12" viewBox="0 0 8 12"><path d="M1 1l5 5-5 5" stroke="#0a9bf2" stroke-width="2" fill="none"/></svg>Supplement List to accelerate<br>metabolism</li>
    <li><svg width="8" height="12" viewBox="0 0 8 12"><path d="M1 1l5 5-5 5" stroke="#0a9bf2" stroke-width="2" fill="none"/></svg>10% off First Supplement<br>Purchase to Kickstart the<br>process</li>
    <li><svg width="8" height="12" viewBox="0 0 8 12"><path d="M1 1l5 5-5 5" stroke="#0a9bf2" stroke-width="2" fill="none"/></svg>Exclusive access to PulseForge’s<br>Private Online Page for<br>additional recipes, Support<br>and Guidance</li>
  </ul>

  <p class="abs price-old">$199</p>
  <div class="abs limited-tag"><span>LIMITED<br>TIME</span></div>
  <div class="abs price-card">
    <span class="cta">GET<br>STARTED<br>NOW</span>
    <span class="amount">$99</span>
  </div>

  <div class="abs brand">
    <p class="brand-name">PulseForge</p>
    <p class="brand-tagline">Personal Group Training</p>
  </div>
</main>
</body>
</html>
```